Need a Brochure Design

We need a brochure designed (A4 two sides or A3 foldable which is equal to 2 x A4 = total of four pages )

Brief and Logo attached.

```html
<!DOCTYPE html>
<html lang="en">
<head>
<meta charset="utf-8">
<title>Stage Smart Homes – Plans &amp; Prices</title>
<link href="https://fonts.googleapis.com/css2?family=DM+Sans:ital,wght@0,300;0,400;0,500;0,600;1,400&display=swap" rel="stylesheet">
<style>
  :root {
    --ink: #1b1b1b;
    --blush: #fde1d7;
    --cream: #fdf4e2;
    --hero-light: #eef0ee;
    --hero-mid: #d9dcd8;
    --room-grey: #c9cbc8;
    --room-warm: #b9ab98;
    --kitchen-light: #e7e6e3;
    --kitchen-dark: #6b5a4c;
  }
  * { margin: 0; padding: 0; box-sizing: border-box; }
  html, body { width: 848px; height: 1200px; overflow: hidden; background: #fff; }
  body { font-family: "DM Sans", sans-serif; color: var(--ink); }
  .brochure { position: relative; width: 848px; height: 1200px; overflow: hidden; }

  .hero {
    position: absolute; left: 0; top: 0; width: 848px; height: 264px;
    background: linear-gradient(100deg, var(--hero-mid) 0%, var(--hero-light) 35%, #f4f4f2 60%, #c8d2c4 100%);
  }
  .hero-title {
    position: absolute; left: 0; width: 848px; top: 83px; text-align: center;
    font-size: 28px; font-weight: 500; letter-spacing: 0.2px;
  }
  .hero-tagline {
    position: absolute; left: 0; width: 848px; top: 130px; text-align: center;
    font-size: 13.5px; line-height: 17px; font-weight: 400;
  }

  .plans { position: absolute; left: 0; top: 264px; width: 848px; height: 266px; background: var(--blush); }
  .plans-heading {
    position: absolute; left: 0; width: 848px; top: 30px; text-align: center;
    font-size: 30px; font-weight: 500;
  }
  .plan { position: absolute; top: 102px; width: 180px; }
  .plan-icons { display: flex; gap: 6px; height: 22px; }
  .plan-icons svg { width: 36px; height: 22px; }
  .plan-name { margin-top: 16px; font-size: 14.5px; font-weight: 500; }
  .plan-detail { margin-top: 2px; font-size: 10.5px; }
  .plan-price { margin-top: 5px; font-size: 14.5px; font-weight: 500; }
  .plans-note {
    position: absolute; left: 0; width: 848px; top: 222px; text-align: center;
    font-size: 10.5px; font-style: italic;
  }

  .photo { position: absolute; }
  .photo-living { left: 0; top: 530px; width: 394px; height: 240px;
    background: linear-gradient(180deg, #eceeed 0%, #dedfdd 55%, var(--room-grey) 75%, var(--room-warm) 100%); }
  .photo-dining { left: 0; top: 771px; width: 199px; height: 139px;
    background: linear-gradient(160deg, #ececea 0%, #d8d6d2 55%, #8a6a4c 100%); }
  .photo-patio { left: 200px; top: 771px; width: 194px; height: 139px;
    background: linear-gradient(180deg, #d8cfc4 0%, #b9b2a8 50%, #7a8a6a 100%); }
  .photo-kitchen { left: 0; top: 911px; width: 394px; height: 289px;
    background: linear-gradient(180deg, #eeeeec 0%, var(--kitchen-light) 55%, #cfcecb 78%, var(--kitchen-dark) 100%); }

  .benefits { position: absolute; left: 394px; top: 530px; width: 454px; height: 425px; background: var(--cream); }
  .benefit-list { position: absolute; left: 46px; top: 45px; width: 300px; list-style: none; }
  .benefit-list li {
    position: relative; padding-left: 13px; margin-bottom: 14px;
    font-size: 16px; line-height: 20px; font-weight: 500;
  }
  .benefit-list li::before { content: "•"; position: absolute; left: 0; top: 0; }

  .contact { position: absolute; left: 394px; top: 955px; width: 454px; height: 245px; background: var(--blush); }
  .contact-lead { position: absolute; left: 44px; top: 46px; font-size: 20px; font-weight: 300; }
  .contact-lines { position: absolute; left: 44px; top: 78px; font-size: 15.5px; line-height: 27px; font-weight: 500; list-style: none; }
  .contact-lines span { font-weight: 400; }
</style>
</head>
<body>
<svg width="0" height="0" style="position:absolute">
  <symbol id="icon-sofa" viewBox="0 0 36 22">
    <g fill="none" stroke="#1b1b1b" stroke-width="1.4" stroke-linejoin="round">
      <rect x="7" y="2" width="22" height="9" rx="2"/>
      <rect x="2" y="8" width="5" height="10" rx="1.5"/>
      <rect x="29" y="8" width="5" height="10" rx="1.5"/>
      <rect x="7" y="11" width="22" height="7"/>
      <line x1="18" y1="11" x2="18" y2="18"/>
      <line x1="10" y1="6" x2="26" y2="6"/>
      <line x1="4" y1="18" x2="4" y2="21"/>
      <line x1="32" y1="18" x2="32" y2="21"/>
    </g>
  </symbol>
</svg>

<main class="brochure">
  <section class="hero" role="img" aria-label="Bright staged living room with kitchen window and indoor plants">
    <h1 class="hero-title">Stage Smart Homes</h1>
    <p class="hero-tagline">We average over 185 property styling<br>projects per year, with a large proportion<br>selling in less than 30 days!</p>
  </section>

  <section class="plans">
    <h2 class="plans-heading">Plans &amp; Prices</h2>

    <div class="plan" style="left:60px">
      <div class="plan-icons"><svg><use href="#icon-sofa"/></svg></div>
      <p class="plan-name">1 Bedroom Property</p>
      <p class="plan-detail">Full Styling + 6 Weeks Free Hire*</p>
      <p class="plan-price">AUD$1,897.00</p>
    </div>
    <div class="plan" style="left:249px">
      <div class="plan-icons"><svg><use href="#icon-sofa"/></svg><svg><use href="#icon-sofa"/></svg></div>
      <p class="plan-name">1 Bedroom Property</p>
      <p class="plan-detail">Full Styling + 6 Weeks Free Hire*</p>
      <p class="plan-price">AUD$2,697.00</p>
    </div>
    <div class="plan" style="left:437px">
      <div class="plan-icons"><svg><use href="#icon-sofa"/></svg><svg><use href="#icon-sofa"/></svg><svg><use href="#icon-sofa"/></svg></div>
      <p class="plan-name">1 Bedroom Property</p>
      <p class="plan-detail">Full Styling + 6 Weeks Free Hire*</p>
      <p class="plan-price">AUD$2,997.00</p>
    </div>
    <div class="plan" style="left:625px">
      <div class="plan-icons"><svg><use href="#icon-sofa"/></svg><svg><use href="#icon-sofa"/></svg><svg><use href="#icon-sofa"/></svg><svg><use href="#icon-sofa"/></svg></div>
      <p class="plan-name">1 Bedroom Property</p>
      <p class="plan-detail">Full Styling + 6 Weeks Free Hire*</p>
      <p class="plan-price">AUD$3,897.00</p>
    </div>

    <p class="plans-note">* 4 Weeks Free Hire + 2 Weeks Free Extension (if property not sold within 4 weeks)</p>
  </section>

  <div class="photo photo-living" role="img" aria-label="Staged living room with grey sofas, cushions and timber coffee table"></div>
  <div class="photo photo-dining" role="img" aria-label="Open-plan dining area with timber table and chairs"></div>
  <div class="photo photo-patio" role="img" aria-label="Covered outdoor patio with lounge chairs and ceiling fan"></div>
  <div class="photo photo-kitchen" role="img" aria-label="White kitchen with marble island, pendant lights and dark timber floor"></div>

  <section class="benefits">
    <ul class="benefit-list">
      <li>Helping your property reach its highest potential without busting the budget.</li>
      <li>Achieving a record number of viewings and the highest possible sale price.</li>
      <li>Installation, interior design and decoration, and removal included.</li>
      <li>Pre-sale home preparation to post-sale removal.</li>
      <li>Free consultation and longer rental periods.</li>
      <li>A small investment for such a large transformation!</li>
    </ul>
  </section>

  <section class="contact">
    <p class="contact-lead">Please contact us at:</p>
    <ul class="contact-lines">
      <li>0400 512 389 <span>or</span></li>
      <li>hello@stagesmarthomes.com.au</li>
      <li>www.stagesmarthomes.com.au</li>
    </ul>
  </section>
</main>
</body>
</html>
```